Roll-Up Banner für Glückswebsite
Zielgruppe
Die Website, www.heiterkompass.de ermöglicht es jedem Interessierten kostenlos mehr über das eigene Lebensglück, persönliche Stärken, und die eigene Lebenszufriedenheit herauszufinden. Interessierte können online Fragebögen ausfüllen, und erhalten neben einer detaillierten Rückmeldung über die eigenen Möglichkeiten und Stärken, Hinweise dazu, wie Sie an Ihrem eigenen Potenzial arbeiten können. Es handelt sich um ein Kooperationsprojekt der Nordischen Vereinigung für Angewandte Seelenkunde der Uni Wolkenrode, der HK-Selmhorst, der Medical School Trebnitz und der Uni Kalbenau. Zielgruppe für das Banner sind Menschen, die selbst mit Klienten im Kontext der Positiven Psychologie arbeiten oder Menschen, die sich Ihrem eigenen Lebensglück zuwenden wollen.
Aufgabenstellung
Es handelt sich um ein Roll-up Banner in den Maßen 1m Breite und 2 Meter Höhe.
Das Banner sollte so angelegt sein, dass es interessierten Besuchern auf Kongressen vermittelt, was es mit der Seite Heiterkompass.de auf sich hat. Also wissenschaftlich evaluierte kostenfreie online-Fragebögen, die Menschen dabei helfen Ihre eigenen Stärken und Potenziale zu entdecken und dem eigenen Glück näher zu kommen.
Es sollte außerdem das Logo der NVAS darauf zu sehen sein, sowie kleiner die Logos der Forschungskooperationspartner, HK-Selmhorst, Uni Wolkenrode, Uni Kalbenau, Medical School Trebnitz.
Die Farben sollten zum Logo der NVAS passen.

```html
<!DOCTYPE html>
<html lang="de">
<head>
<meta charset="utf-8">
<title>Roll-Up Banner – Heiterkompass</title>
<link rel="stylesheet" href="https://fonts.googleapis.com/css2?family=Signika:wght@500;600&family=Noto+Sans:wght@300;400&display=swap">
<style>
  :root {
    --green: #6cb85f;
    --teal: #2aa3bd;
    --teal-mid: #3aa49a;
    --navy: #1c3a6e;
    --navy-deep: #0e2a5c;
    --paper: #f3f4f6;
    --footer: #e4e6ea;
    --stage: #dfe2e7;
    --white: #ffffff;
    --dot-1: #7cc3d8;
    --dot-2: #25a095;
    --dot-3: #2a9a62;
    --dot-4: #1e3f73;
  }
  * { box-sizing: border-box; margin: 0; padding: 0; }
  html, body { width: 768px; height: 1200px; overflow: hidden; }
  body { background: var(--stage); font-family: "Noto Sans", sans-serif; }

  .banner {
    position: absolute; left: 78px; top: 0;
    width: 612px; height: 1200px;
    background: var(--paper);
    overflow: hidden;
  }

  .url-band {
    position: absolute; left: 0; top: 0; width: 100%; height: 125px;
    background: linear-gradient(90deg, var(--green), var(--teal));
  }
  .url-band__text {
    position: absolute; left: 44px; top: 46px;
    font-family: "Signika", sans-serif; font-weight: 600;
    font-size: 48px; letter-spacing: -1.2px; line-height: 1;
    color: var(--white);
  }

  .hero { position: absolute; left: 0; top: 125px; width: 100%; height: 333px; background: var(--paper); }
  .hero__photo {
    position: absolute; right: 0; top: 0; width: 400px; height: 100%;
    background:
      radial-gradient(ellipse 45% 55% at 62% 40%, #e0b395 0%, rgba(224,179,149,0) 70%),
      linear-gradient(90deg, rgba(243,244,246,1) 0%, rgba(200,190,176,.6) 30%, #b49a80 60%, #7d6a58 100%);
  }
  .brand { position: absolute; left: 44px; top: 40px; }
  .brand__name {
    display: flex; align-items: center; gap: 8px;
    font-family: "Signika", sans-serif; font-weight: 600;
    font-size: 22px; letter-spacing: 2px; color: var(--navy);
  }
  .brand__mark { width: 14px; height: 14px; border-radius: 50%; background: var(--teal-mid); }
  .brand__sub { margin-top: 6px; font-size: 9.5px; line-height: 1.3; color: var(--navy); }
  .hero__headline {
    position: absolute; left: 41px; top: 206px;
    font-family: "Signika", sans-serif; font-weight: 600;
    font-size: 37px; line-height: 49px; color: var(--navy);
  }

  .info {
    position: absolute; left: 0; top: 458px; width: 100%; height: 587px;
    background: linear-gradient(200deg, var(--teal) 0%, var(--teal-mid) 55%, var(--green) 100%);
    color: var(--white);
  }
  .info__intro {
    position: absolute; left: 44px; top: 40px; width: 520px;
    font-size: 16.5px; line-height: 23.5px; font-weight: 300;
  }
  .steps { position: absolute; left: 0; top: 0; width: 100%; height: 100%; }
  .steps__line { position: absolute; left: 58px; top: 187px; width: 2px; height: 237px; background: rgba(255,255,255,.8); }
  .step { position: absolute; left: 0; }
  .step__dot {
    position: absolute; left: 45px; width: 28px; height: 28px; border-radius: 50%;
    border: 2px solid var(--white);
  }
  .step__title { position: absolute; left: 104px; white-space: nowrap; font-size: 24px; font-weight: 300; line-height: 1; }
  .step__note { position: absolute; left: 104px; white-space: nowrap; font-size: 17px; font-weight: 300; line-height: 1; }

  .badge {
    position: absolute; left: 430px; top: 254px; width: 184px; height: 52px;
    background: var(--navy-deep); transform: rotate(-2deg);
    display: flex; flex-direction: column; justify-content: center; align-items: center;
    font-size: 12.5px; line-height: 17px; font-weight: 300;
  }

  .rule { position: absolute; left: 0; top: 1045px; width: 100%; height: 6px; background: var(--navy-deep); }

  .partners { position: absolute; left: 0; top: 1051px; width: 100%; height: 149px; background: var(--footer); }
  .partners__title { position: absolute; left: 44px; top: 22px; font-size: 17px; color: var(--navy); }
  .partner {
    position: absolute; top: 84px; display: flex; align-items: center; gap: 6px;
    font-size: 10.5px; color: var(--navy); white-space: nowrap;
  }
  .partner__mark { width: 10px; height: 10px; border-radius: 50%; background: var(--navy); }
</style>
</head>
<body>
  <main class="banner">
    <header class="url-band">
      <div class="url-band__text">www.heiterkompass.de</div>
    </header>

    <section class="hero">
      <div class="hero__photo" role="img" aria-label="Foto: lachender junger Mann mit Brille und kariertem Hemd"></div>
      <div class="brand">
        <div class="brand__name"><span class="brand__mark"></span>NVAS</div>
        <div class="brand__sub">Nordische Vereinigung für<br>Angewandte Seelenkunde</div>
      </div>
      <h1 class="hero__headline">Kennen Sie sich<br>und Ihre Stärken?</h1>
    </section>

    <section class="info">
      <p class="info__intro">Unter www.heiterkompass.de haben Sie die Möglichkeit kostenfrei die neusten wissenschaftlichen Fragebögen im Bereich der Positiven Psychologie zu nutzen und ein detailliertes Feedback zu Ihren Ergebnissen zu erhalten.</p>

      <div class="steps">
        <div class="steps__line"></div>
        <div class="step" style="top:0">
          <span class="step__dot" style="top:173px;background:var(--dot-1)"></span>
          <span class="step__title" style="top:175px">Registrieren</span>
          <span class="step__note" style="top:211px">– und damit immer Zugriff auf Ihre Ergebnisse haben</span>
        </div>
        <div class="step" style="top:0">
          <span class="step__dot" style="top:262px;background:var(--dot-2)"></span>
          <span class="step__title" style="top:264px">Online-Fragebogen ausfüllen</span>
          <span class="step__note" style="top:300px">unter www.heiterkompass.de</span>
        </div>
        <div class="step" style="top:0">
          <span class="step__dot" style="top:352px;background:var(--dot-3)"></span>
          <span class="step__title" style="top:354px">Persönliche Rückmeldung erhalten</span>
        </div>
        <div class="step" style="top:0">
          <span class="step__dot" style="top:410px;background:var(--dot-4)"></span>
          <span class="step__title" style="top:412px">Ein noch erfüllteres Leben gestalten</span>
        </div>
      </div>

      <div class="badge"><span>wissenschaftlich evaluiert</span><span>kostenfrei | anonym</span></div>
    </section>

    <div class="rule"></div>

    <footer class="partners">
      <div class="partners__title">Forschungskooperationspartner</div>
      <div class="partner" style="left:44px"><span class="partner__mark"></span>Uni Wolkenrode</div>
      <div class="partner" style="left:150px"><span class="partner__mark"></span>Medical School Trebnitz</div>
      <div class="partner" style="left:300px"><span class="partner__mark"></span>HK-Selmhorst</div>
      <div class="partner" style="left:464px"><span class="partner__mark"></span>Uni Kalbenau</div>
    </footer>
  </main>
</body>
</html>
```